Morvex Business Card (intended for Business Card sized magnet)

Hi guys,

I would like to get a design for my business card for the restaurant. The design must be single sided as I intend to produce business card sized magnets.

The File attached must me on and I'm open for new ides

Can you please ensure that the design meets Cardowell's magnetic business card size specifications:

http://www.cardowell.example.au/custom-magnets.aspx?txi=15695&xnid=TopNav_Magnetic+Business+Cards+(linked+item)_Magnets_Marketing+Products&xnav=TopNav

Full Bleed Size (starting document size):
90 x 52 mm
1062 x 615 pixels
* Finished artwork should use the full bleed dimensions for best results.

Document Trim Size (final size after being cut):
87 x 49 mm
1028 x 579 pixels
* Please be sure to keep all text within the safe margin.

Resolution:
300 DPI

The winning design/source files need to meet these specifications.

Thanks
Updates

Hi guys, can I see more options please Thanks

```html
<!DOCTYPE html>
<html lang="en">
<head>
<meta charset="utf-8">
<title>Morvex Business Card</title>
<link rel="stylesheet" href="https://fonts.googleapis.com/css2?family=Cardo&family=Alegreya+Sans:wght@500&display=swap">
<style>
  :root {
    --backdrop: #f1f0ee;
    --card-dark: #1f1c1a;
    --card-cream: #f4dca2;
    --card-cream-deep: #ecd08c;
    --gold: #e9cf95;
    --ink: #1a1816;
    --band-light: #c9ad72;
    --band-dark: #2c2620;
  }
  * { margin: 0; padding: 0; box-sizing: border-box; }
  html, body {
    width: 1200px;
    height: 1000px;
    overflow: hidden;
    background: var(--backdrop);
  }
  .card {
    position: absolute;
    left: 120px;
    top: 222px;
    width: 960px;
    height: 556px;
    overflow: hidden;
    background: var(--card-cream);
  }
  .card__dark-panel {
    position: absolute;
    left: 0; top: 0;
    width: 460px; height: 100%;
    background: var(--card-dark);
  }
  .card__texture {
    position: absolute;
    left: 460px; top: 0;
    width: 500px; height: 100%;
    background: radial-gradient(ellipse at 60% 40%, var(--card-cream) 0%, var(--card-cream-deep) 100%);
  }
  .brand-name {
    position: absolute;
    right: 526px;
    top: 268px;
    font-family: "Cardo", serif;
    font-weight: 400;
    font-size: 96px;
    line-height: 1;
    color: var(--gold);
    letter-spacing: 1px;
    white-space: nowrap;
  }
  .ornament-band {
    position: absolute;
    left: 100px;
    top: 370px;
    width: 790px;
    height: 120px;
  }
  .ornament-band__fill {
    position: absolute;
    left: 0; top: 12px;
    width: 100%; height: 96px;
    background: linear-gradient(90deg, var(--band-light) 0%, var(--band-light) 45%, var(--band-dark) 55%, var(--band-dark) 100%);
  }
  .ornament-band__rule {
    position: absolute;
    left: 0;
    width: 100%;
    height: 3px;
    background: linear-gradient(90deg, var(--gold) 0%, var(--gold) 46%, var(--ink) 46%, var(--ink) 100%);
  }
  .ornament-band__rule--top { top: 0; }
  .ornament-band__rule--bottom { bottom: 0; }
  .contact {
    position: absolute;
    left: 500px;
    top: 150px;
    font-family: "Alegreya Sans", sans-serif;
    font-style: normal;
    font-weight: 500;
    font-size: 28px;
    line-height: 1.2;
    color: var(--ink);
  }
  .contact__address {
    display: flex;
    align-items: flex-start;
    gap: 6px;
  }
  .contact__pin { width: 20px; height: 28px; margin-top: 3px; flex: none; }
  .contact__address-lines span { display: block; }
  .contact__address-lines span + span { padding-left: 12px; }
  .contact__phone { margin-top: 20px; }
  .contact__email { margin-top: 22px; }
  .website {
    position: absolute;
    left: 600px;
    top: 502px;
    font-family: "Alegreya Sans", sans-serif;
    font-weight: 500;
    font-size: 26px;
    color: var(--ink);
  }
</style>
</head>
<body>
  <section class="card" aria-label="Morvex business card">
    <div class="card__dark-panel"></div>
    <div class="card__texture" role="img" aria-label="Faint cream swirl pattern background"></div>

    <h1 class="brand-name">Morvex</h1>

    <div class="ornament-band">
      <div class="ornament-band__rule ornament-band__rule--top"></div>
      <div class="ornament-band__fill" role="img" aria-label="Geometric star lattice ornament with red, teal and yellow centres"></div>
      <div class="ornament-band__rule ornament-band__rule--bottom"></div>
    </div>

    <address class="contact">
      <div class="contact__address">
        <svg class="contact__pin" viewBox="0 0 22 30" aria-hidden="true">
          <path d="M11 1C5.5 1 1 5.4 1 10.8 1 18 11 29 11 29s10-11 10-18.2C21 5.4 16.5 1 11 1z" fill="#1a1816"/>
          <circle cx="11" cy="10.5" r="3.8" fill="#f4dca2"/>
        </svg>
        <div class="contact__address-lines">
          <span>412 Harwell st,</span>
          <span>linden park, 3190</span>
        </div>
      </div>
      <div class="contact__phone">03 9410 2837</div>
      <div class="contact__email">Morvex412@mailbox.example</div>
    </address>

    <div class="website">www.morvex.example.au</div>
  </section>
</body>
</html>
```